Lunora Vaginal Suppositories eCommerce Website Design

We are designing an ecommerce website for a new company and product. The product is vaginal moisturizer suppositories. We are going to develop this site on Shopify so you can add in any featured you have knowledge of in Shopify.

We are purposefully not adding any images to allow you to create something with your style. A similar product is petalkind.example. We would like a site similar to this in style, but obviously different not to look the same. It is a product for women so it needs to be a very feminine theme. We have had designers use thier own illustrations in previous designs that looked great, or stock images that don't look "stock" would be good. We would like the product section to look like a normal product section on Shopify, specified in the link below. The rest of the site with the featues and benefits and ingredients can be displayed creatively with images, illustrations, or product placement interspersed. Use any high quality images you have access to and we will purchase if necessary.

Use icons and symbols to represent the different benefits and ingredients.

Pay no attention to colors in the wireframe. The only defitinte color is the logo.

I put a picture of the actual suppositories so we would like to intersperse that (an individual one, not inside the package) in a few places. You can use it in the directions section for sure.

Video about wireframe: https://files.example-share.net/d/Xq82mLp0Tz/view

https://slides.example-share.net/p/Rk47vNw2Hc/edit

Target Market(s)

Women

Industry/Entity Type

Healthcare

Number of Pages Required

1 page

Requirements
Must have
• I added a "wireframe" in the description
Nice to have
Should not have

```html
<!DOCTYPE html>
<html lang="en">
<head>
<meta charset="utf-8">
<title>Lunora Vaginal Suppositories</title>
<link rel="stylesheet" href="https://fonts.googleapis.com/css2?family=Fraunces:opsz,wght@9..144,400;9..144,500;9..144,600&family=Jost:wght@400;500&display=swap">
<style>
:root{
  --topbar:#f0c4c6;
  --ink:#3e2a28;
  --brown:#5b302c;
  --magenta:#d42a8a;
  --coral:#d4524a;
  --gold:#9c7026;
  --hero-a:#f6d6d6;
  --hero-b:#f9e4e2;
  --panel:#f3e9ef;
  --line:#ddd2d4;
  --card1:#ecdfea;
  --card2:#f3ecef;
  --card3:#fbe7e1;
  --card4:#e5eddf;
  --txt1:#8a6bb3;
  --txt2:#6e5d5d;
  --txt3:#c68f38;
  --txt4:#7c9f4d;
}
*{box-sizing:border-box;margin:0;padding:0}
html,body{width:1200px;height:800px;overflow:hidden;background:#fff}
body{position:relative;font-family:"Jost",sans-serif;color:var(--ink)}
.topbar{position:absolute;left:0;top:0;width:1200px;height:34px;background:var(--topbar);display:flex;justify-content:center;align-items:center;font-size:11.5px;letter-spacing:.6px;color:#3d2826}
.topbar span{padding:0 13px;border-right:1px solid #a27877;line-height:22px}
.topbar span:last-child{border-right:none}
.nav{position:absolute;left:0;top:34px;width:1200px;height:72px}
.logo{position:absolute;left:30px;top:20px;font-family:"Jost",sans-serif;font-weight:500;font-size:29px;color:var(--magenta);display:flex;align-items:center;gap:6px}
.logo i{width:9px;height:9px;border-radius:50%;background:var(--magenta);display:block}
.menu{position:absolute;left:388px;top:30px;display:flex;gap:30px;font-size:13px;letter-spacing:.6px}
.menu a{color:var(--ink);text-decoration:none}
.menu a.active{border-bottom:2px solid var(--gold);padding-bottom:8px}
.nav-icon{position:absolute;left:968px;top:29px}
.signin{position:absolute;left:1028px;top:20px;width:120px;height:33px;border:1px solid #6b5a58;border-radius:17px;font-size:12.5px;letter-spacing:.6px;display:flex;align-items:center;justify-content:center}
.account{position:absolute;left:1162px;top:24px;width:26px;height:26px;border:1.5px solid #6b5a58;border-radius:50%}
.hero{position:absolute;left:5px;top:118px;width:769px;height:371px;border-radius:14px;background:linear-gradient(100deg,var(--hero-a),var(--hero-b));overflow:hidden}
.hero h1{position:absolute;left:45px;top:70px;width:380px;font-family:"Fraunces",serif;font-weight:500;font-size:49px;line-height:51px;color:var(--brown);letter-spacing:-.5px}
.hero .sub{position:absolute;left:45px;top:236px;font-family:"Fraunces",serif;font-size:18px;color:#4e3431}
.hero .cta{position:absolute;left:45px;top:277px;width:168px;height:39px;border-radius:20px;background:var(--coral);color:#fff;font-size:12.5px;letter-spacing:.4px;display:flex;align-items:center;justify-content:center}
.hero-photo{position:absolute;left:420px;top:0;width:349px;height:371px;background:radial-gradient(ellipse at 55% 55%,#f6cbbf 0%,#f8dcd6 45%,rgba(249,228,226,0) 75%)}
.buy{position:absolute;left:781px;top:118px;width:414px;height:371px;border-radius:14px;background:var(--panel)}
.buy-card{position:absolute;left:30px;top:26px;width:354px;height:320px;background:#fff;border-radius:10px;padding:0 13px}
.buy-card .head{font-size:12.5px;letter-spacing:.5px;text-align:center;padding:13px 0 12px;border-bottom:1px solid var(--line)}
.select{display:flex;justify-content:space-between;align-items:center}
.select.title{margin-top:18px;font-family:"Fraunces",serif;font-size:20px;color:var(--gold)}
.select.opt{margin-top:14px;font-family:"Fraunces",serif;font-size:14px;line-height:23px;color:#c27c55}
.select svg{flex:none}
.qty-label{margin-top:23px;font-size:10px;letter-spacing:.4px;color:#c7b7c2}
.swatches{margin-top:8px;display:flex;align-items:center;justify-content:space-between}
.dots{display:flex;gap:2px}
.dots b{width:16px;height:16px;border-radius:50%;border:1px solid #b9aaa8;display:block}
.dots b.on{background:var(--gold);border-color:var(--gold)}
.circles{display:flex;gap:4px}
.circles b{width:31px;height:31px;border-radius:50%;display:block}
.btn-outline{margin-top:13px;height:34px;border:1px solid #c9b9bb;border-radius:17px;font-size:11.5px;letter-spacing:.4px;display:flex;align-items:center;justify-content:center}
.btn-solid{margin-top:10px;height:34px;border-radius:17px;background:var(--gold);color:#fff;font-size:11.5px;letter-spacing:.4px;display:flex;align-items:center;justify-content:center}
.features{position:absolute;left:5px;top:496px;display:flex;gap:7px}
.feature{width:294px;height:291px;border-radius:14px;text-align:center;padding-top:35px}
.feature .ico{width:54px;height:54px;border-radius:50%;margin:0 auto;display:flex;align-items:center;justify-content:center}
.feature h3{margin:22px auto 0;width:250px;font-family:"Fraunces",serif;font-weight:500;font-size:18px;line-height:24px;color:var(--brown);height:76px}
.feature p{margin:12px auto 0;width:210px;font-family:"Fraunces",serif;font-size:14px;line-height:21px}
.f1{background:var(--card1)}.f1 p{color:var(--txt1)}
.f2{background:var(--card2)}.f2 p{color:var(--txt2)}
.f3{background:var(--card3)}.f3 p{color:var(--txt3)}
.f4{background:var(--card4)}.f4 p{color:var(--txt4)}
.ico{background:rgba(255,255,255,.5)}
</style>
</head>
<body>
<div class="topbar"><span>FREE SHIPPING</span><span>VEGAN &amp; HORMONE FREE INGREDIENTS</span><span>SHOP ONLINE TODAY</span></div>

<header class="nav">
  <div class="logo"><i></i>Lunora</div>
  <nav class="menu"><a class="active">SHOP</a><a>BENEFITS</a><a>INGREDIENTS</a><a>ABOUT</a><a>CONTACT</a></nav>
  <svg class="nav-icon" width="30" height="18" viewBox="0 0 30 18"><g stroke="#5e4c4a" stroke-width="1.5" fill="none"><path d="M1 4h12M1 9h10M1 14h12"/><circle cx="21" cy="10" r="5"/></g></svg>
  <div class="signin">SIGN IN</div>
  <div class="account"></div>
</header>

<section class="hero">
  <div class="hero-photo" role="img" aria-label="Photo of hands holding a white moisturizing suppository"></div>
  <h1>Your vaginal comfort for ease and softness</h1>
  <div class="sub">Welcome to petalkind.example</div>
  <div class="cta">PRODUCTS SHOP</div>
</section>

<aside class="buy">
  <div class="buy-card">
    <div class="head">PRODUCT FOR SUBSCRIPTION SAVINGS</div>
    <div class="select title">Suppositories<svg width="12" height="8" viewBox="0 0 12 8"><path d="M1 1l5 5 5-5" stroke="#6b5a58" stroke-width="1.4" fill="none"/></svg></div>
    <div class="select opt"><span>Choose your daily moisturizing routine for •<br>Subscription options</span><svg width="12" height="8" viewBox="0 0 12 8"><path d="M1 1l5 5 5-5" stroke="#6b5a58" stroke-width="1.4" fill="none"/></svg></div>
    <div class="qty-label">QUANTITY</div>
    <div class="swatches">
      <div class="dots"><b></b><b></b><b class="on"></b><b></b><b></b><b></b></div>
      <div class="circles"><b style="background:#d4524a"></b><b style="border:1px solid #d4524a"></b><b style="background:#d4524a"></b><b style="background:#efe5ee"></b></div>
    </div>
    <div class="btn-outline">ADD TO BASKET</div>
    <div class="btn-solid">SHOP NOW</div>
  </div>
</aside>

<section class="features">
  <article class="feature f1">
    <div class="ico"><svg width="30" height="30" viewBox="0 0 30 30" fill="none" stroke="#6a3a38" stroke-width="1.4"><circle cx="15" cy="8" r="5"/><circle cx="8" cy="16" r="5"/><circle cx="22" cy="16" r="5"/><circle cx="15" cy="23" r="5"/></svg></div>
    <h3>Features, Benefits, Ingredients &amp; Subscription Savings</h3>
    <p>Your natural moisture routine made simple with every monthly delivery.</p>
  </article>
  <article class="feature f2">
    <div class="ico"><svg width="30" height="30" viewBox="0 0 30 30" fill="none" stroke="#6a3a38" stroke-width="1.4"><path d="M8 12h14v10a4 4 0 0 1-4 4h-6a4 4 0 0 1-4-4z"/><path d="M19 12l3-7"/></svg></div>
    <h3>Features that soothe, Your Recommended Suppositories</h3>
    <p>Your gentle daily relief with pure ingredients for lasting comfort.</p>
  </article>
  <article class="feature f3">
    <div class="ico"><svg width="30" height="30" viewBox="0 0 30 30" fill="none" stroke="#9c7026" stroke-width="1.4"><path d="M15 15C11 9 12 4 15 2c3 2 4 7 0 13zM15 15c-4 6-3 11 0 13 3-2 4-7 0-13zM15 15c-6-4-11-3-13 0 2 3 7 4 13 0zM15 15c6-4 11-3 13 0-2 3-7 4-13 0z"/></svg></div>
    <h3>Your Everyday Comfort and Confidence</h3>
    <p>Your daily comfort in a natural balance with soft botanical care.</p>
  </article>
  <article class="feature f4">
    <div class="ico"><svg width="30" height="30" viewBox="0 0 30 30" fill="none" stroke="#7a5a2a" stroke-width="1.4"><path d="M6 25C6 12 14 5 25 5c0 12-7 20-19 20z"/><path d="M6 25L19 11"/></svg></div>
    <h3>Welcome relief at Your Own Pace</h3>
    <p>Your care in a natural form with nourishing plant extracts.</p>
  </article>
</section>
</body>
</html>
```